CSS Template Layout

We are looking for a page design template that we can update our site. Here are the requirements.

We need a header image across the top and three columns below. Layout should be controlled by css, not tables.

This is for a landscape/snow removal directory. A generic layout for overall size can be found at www.brindlemowpath.net Images should relate to lawns/landscaping/snow removal.

We do not have a logo at this time, so we will simply be using a font with the site name. The site should be colorful and inviting, it should feel fresh and clean. These are landscapers and they groom the beauty found in nature.

Do not hesitate to ask questions or bounce ideas off of us.

Project Deadline Extended
Reason: We are sorry but we need to extend the deadline, we inadvertently deadlined on a Saturday and will not be in the office. We have internally worked out our schedules to meet next thursday. On the plus side, we are guaranteeing payment based on the two designs submitted already.

```html
<!DOCTYPE html>
<html lang="en">
<head>
<meta charset="utf-8">
<title>Local Landscape Service</title>
<link rel="stylesheet" href="https://fonts.googleapis.com/css2?family=Open+Sans:ital,wght@0,300;0,400;0,600;0,700;1,400&family=Playfair+Display&family=Lora:ital@1&display=swap">
<style>
:root{
  --grass-dark:#2f7d1c;
  --grass-mid:#4ea52c;
  --grass-light:#5fb83a;
  --white:#ffffff;
  --ink:#222222;
  --text:#555555;
  --muted:#8a8a8a;
  --nav:#3a3e46;
  --nav-dark:#2c3037;
  --intro-bg:#eef3ea;
  --btn-dark:#3b3d41;
  --green:#68bf4a;
  --rule:#e4e4e4;
  --thumb:#777777;
  --quote-bg:#f4f4f4;
  --footer:#363636;
  --footer-text:#d8d8d8;
  --link-green:#3dae2b;
}
*{box-sizing:border-box;margin:0;padding:0}
html,body{width:720px;height:1200px;overflow:hidden}
body{
  position:relative;
  font-family:"Open Sans",Arial,sans-serif;
  color:var(--text);
}
.lawn-backdrop{
  position:absolute;inset:0;
  background:radial-gradient(ellipse at 50% 40%,var(--grass-light),var(--grass-mid) 55%,var(--grass-dark));
}
.page{
  position:absolute;left:60px;top:72px;width:600px;height:1050px;
  background:var(--white);
}
.edge{position:absolute;left:0;width:600px;height:6px;display:block}
.edge-top{top:-5px}
.edge-footer{top:938px}
.inner{position:absolute;left:17px;width:566px}

/* header */
.masthead{top:34px;height:40px}
.site-name{
  font-family:"Playfair Display",Georgia,serif;font-weight:400;
  font-size:18px;letter-spacing:.3px;color:var(--ink);line-height:20px;
}
.tagline{font-size:9.5px;color:var(--muted);line-height:12px}
.contact{position:absolute;right:6px;top:12px;display:flex;gap:22px;font-size:8.5px;color:var(--muted)}
.contact span{display:flex;align-items:center;gap:8px}
.contact svg{width:11px;height:11px}

/* nav */
.main-nav{
  top:79px;height:35px;
  background:linear-gradient(var(--nav),var(--nav-dark));
  display:flex;align-items:center;padding-left:20px;gap:20px;
}
.main-nav a{color:#fff;font-size:9px;text-decoration:none}

/* hero */
.hero{top:114px;height:263px;overflow:hidden}
.hero-photo{
  position:absolute;inset:0;
  background:linear-gradient(180deg,#3a98d8 0%,#7cc2ec 45%,#5aa73a 66%,#3b8d22 100%);
}
.hero-title{
  position:absolute;left:21px;bottom:20px;
  font-size:21px;font-weight:700;color:#fff;
}
.hero-dots{position:absolute;right:11px;bottom:11px;display:flex;gap:6px}
.hero-dots i{width:5px;height:5px;border-radius:50%;background:#fff;display:block}

/* intro */
.intro{top:377px;height:90px;background:var(--intro-bg);display:flex;align-items:center;justify-content:space-between;padding:0 18px 0 21px}
.intro p{font-size:17px;font-weight:300;line-height:18px;color:#5a5f5a;width:370px}
.btn-dark{
  width:138px;height:30px;background:var(--btn-dark);border:1px solid #222;border-radius:2px;
  color:#fff;font-size:11px;font-weight:600;display:flex;align-items:center;justify-content:center;
}

/* services */
.services{top:496px;height:130px;display:flex;gap:13px}
.service{width:180px;position:relative}
.service h2{font-size:14.5px;font-weight:600;color:var(--ink);line-height:20px;margin-bottom:9px}
.service p{font-size:8.6px;line-height:14.3px;color:var(--text)}
.btn-green{
  position:absolute;right:0;top:111px;width:84px;height:18px;background:var(--green);
  color:#fff;font-size:8.5px;display:flex;align-items:center;justify-content:center;
}

/* listings */
.section-title{font-size:10.5px;font-weight:600;color:var(--ink);line-height:14px;padding-bottom:8px;border-bottom:1px solid var(--rule)}
.featured{top:667px;width:371px}
.listing-grid{display:grid;grid-template-columns:193px 178px;row-gap:18px;margin-top:12px}
.listing{display:flex;gap:6px}
.listing .thumb{width:48px;height:48px;background:var(--thumb);flex:none}
.listing h3{font-size:8.3px;font-weight:700;color:var(--ink);line-height:12px;margin-top:1px}
.listing p{font-size:8.3px;line-height:11px;color:var(--text)}
.browse{top:667px;left:402px;width:181px}
.browse ul{list-style:none;margin-top:11px}
.browse li{font-size:8.3px;line-height:18px;color:var(--text)}

/* testimonial */
.testimonial{position:absolute;left:0;top:852px;width:600px;height:91px;background:var(--quote-bg);text-align:center;padding-top:18px}
.testimonial blockquote{font-family:"Lora",Georgia,serif;font-style:italic;font-size:10.6px;line-height:15px;color:#8a8a8a;width:480px;margin:0 auto}
.testimonial cite{display:block;font-style:normal;font-size:8.3px;font-weight:700;color:var(--ink);margin-top:10px}
.testimonial cite a{color:var(--link-green);text-decoration:none}

/* footer */
.site-footer{position:absolute;left:0;top:943px;width:600px;height:107px;background:var(--footer);text-align:center;padding-top:24px}
.footer-nav{display:flex;justify-content:center;gap:20px;font-size:8.3px;color:var(--footer-text);padding-left:6px}
.copyright{font-size:6.6px;color:#aaaaaa;margin-top:8px}
.social{display:flex;justify-content:center;gap:13px;margin-top:14px}
.social i{width:11px;height:11px;border-radius:50%;background:#8c8c8c;display:block}
</style>
</head>
<body>
<div class="lawn-backdrop" role="img" aria-label="Close-up texture of fresh green lawn grass"></div>

<div class="page">
  <svg class="edge edge-top" viewBox="0 0 600 6" preserveAspectRatio="none" aria-hidden="true">
    <defs><pattern id="teeth-top" width="6" height="6" patternUnits="userSpaceOnUse"><polygon points="0,6 3,1 6,6" fill="#ffffff"/></pattern></defs>
    <rect width="600" height="6" fill="url(#teeth-top)"/>
  </svg>

  <header class="inner masthead">
    <h1 class="site-name">LOCAL LANDSCAPE SERVICE</h1>
    <p class="tagline">An Organized Landscape Service Directory</p>
    <div class="contact">
      <span><svg viewBox="0 0 12 12"><path d="M2 1l2.5 0 1 3-1.5 1c.6 1.3 1.7 2.4 3 3l1-1.5 3 1V10c0 .6-.5 1-1 1C5 11 1 7 1 2c0-.5.4-1 1-1z" fill="#333"/></svg>(555) 014-2290</span>
      <span><svg viewBox="0 0 12 12"><rect x="3" y="1" width="6" height="3" fill="#333"/><rect x="1" y="4" width="10" height="5" rx="1" fill="#333"/><rect x="3" y="7" width="6" height="4" fill="#333" stroke="#fff" stroke-width=".8"/></svg>(555) 014-2290</span>
    </div>
  </header>

  <nav class="inner main-nav">
    <a href="#">Home</a><a href="#">About</a><a href="#">Contact</a><a href="#">Register</a><a href="#">Search</a>
  </nav>

  <section class="inner hero">
    <div class="hero-photo" role="img" aria-label="Landscaper riding a lawn mower across a bright green lawn under a blue sky"></div>
    <h2 class="hero-title">Lawn Care Services</h2>
    <div class="hero-dots"><i></i><i></i><i></i><i></i></div>
  </section>

  <section class="inner intro">
    <p>We are organized web directory of local landscape, snow removal and lawn service companies</p>
    <div class="btn-dark">Check Directory</div>
  </section>

  <section class="inner services">
    <article class="service">
      <h2>Lawn care service</h2>
      <p>Consetetur sadipscing elitr, sed diam nonumy eirmod tempor invidunt ut labore et dolore magna aliquyam erat, sed diam voluptua. At vero eos et accusam et justo duo dolores et ea rebum.</p>
      <div class="btn-green">Find Business</div>
    </article>
    <article class="service">
      <h2>Landscaping service</h2>
      <p>Consetetur sadipscing elitr, sed diam nonumy eirmod tempor invidunt ut labore et dolore magna aliquyam erat, sed diam voluptua. At vero eos et accusam et justo duo dolores et ea rebum.</p>
      <div class="btn-green">Find Business</div>
    </article>
    <article class="service">
      <h2>Snow removal service</h2>
      <p>Consetetur sadipscing elitr, sed diam nonumy eirmod tempor invidunt ut labore et dolore magna aliquyam erat, sed diam voluptua. At vero eos et accusam et justo duo dolores et ea rebum.</p>
      <div class="btn-green">Find Business</div>
    </article>
  </section>

  <section class="inner featured">
    <h2 class="section-title">Featured Listings</h2>
    <div class="listing-grid">
      <div class="listing"><div class="thumb" role="img" aria-label="Business photo"></div><div><h3>Rolling Acre Lawn care</h3><p>Brookfield's Premier Landscaping Company</p></div></div>
      <div class="listing"><div class="thumb" role="img" aria-label="Business photo"></div><div><h3>Rolling Acre Lawn care</h3><p>Brookfield's Premier Landscaping Company</p></div></div>
      <div class="listing"><div class="thumb" role="img" aria-label="Business photo"></div><div><h3>Rolling Acre Lawn care</h3><p>Brookfield's Premier Landscaping Company</p></div></div>
      <div class="listing"><div class="thumb" role="img" aria-label="Business photo"></div><div><h3>Rolling Acre Lawn care</h3><p>Brookfield's Premier Landscaping Company</p></div></div>
    </div>
  </section>

  <aside class="inner browse">
    <h2 class="section-title">Browse Businesses</h2>
    <ul>
      <li>Landscape Service (2)</li>
      <li>Lawn Service (2)</li>
      <li>Snow Removal Service (1)</li>
      <li>Tree Service (1)</li>
    </ul>
  </aside>

  <section class="testimonial">
    <blockquote>Duis autem vel eum iriure dolor in hendrerit in vulputate velit esse molestie consequat, vel illum dolore eu feugiat nerit in vulputate velit esse molesulla facilisis.</blockquote>
    <cite>Business Owner &nbsp;- <a href="#">www.greenverge-demo.com</a></cite>
  </section>

  <footer class="site-footer">
    <nav class="footer-nav"><span>Home</span><span>Landscape Service</span><span>Lawn Service</span><span>Snow Removal Service</span><span>Contact Us</span></nav>
    <p class="copyright">©Copyright 2013 Local Landscape Services Directory</p>
    <div class="social"><i></i><i></i><i></i><i></i></div>
  </footer>

  <svg class="edge edge-footer" viewBox="0 0 600 6" preserveAspectRatio="none" aria-hidden="true">
    <defs><pattern id="teeth-foot" width="6" height="6" patternUnits="userSpaceOnUse"><polygon points="0,0 3,5 6,0" fill="#f4f4f4"/><polygon points="0,6 3,5 6,6 6,0 3,5 0,0" fill="#363636"/></pattern></defs>
    <rect width="600" height="6" fill="url(#teeth-foot)"/>
  </svg>
</div>
</body>
</html>
```